Business card design needed

I have a leadership coaching and consultancy business which specialises in the education sector. I would like a clean, professional design). The design needs to speak to strength, support, new learning, connections & a growth mindest.

I am also looking for a unique LOGO. This is very important.

Target Market(s)

Educational Leaders & executives

Industry/Entity Type

Leadership

Contact Information for Business Card

Miranda Voss
Principal Coach & Consultant
Miranda Voss Coaching & Consulting
0491 362 815
miranda.voss@quillmail.example
I also would like my facebook, twitter and linkedin accounts to appear

Logo styles of interest
Lettermark Logo
Requirements
Must have
• A 2 sided business card with contact details on the back
A logo

```html
<!DOCTYPE html>
<html lang="en">
<head>
<meta charset="utf-8">
<title>Miranda Voss – Business Card</title>
<link rel="stylesheet" href="https://fonts.googleapis.com/css2?family=Open+Sans:wght@700&family=PT+Sans+Narrow:wght@400&display=swap">
<style>
  :root {
    --page: #ffffff;
    --card: #f7dfc6;
    --card-light: #f8e4c9;
    --ink: #2b2118;
    --accent: #e2620f;
    --band-orange: #b85a0e;
    --band-orange-edge: #6a3306;
    --band-grey: #2f3537;
    --band-grey-edge: #1c2021;
  }
  html, body {
    margin: 0;
    padding: 0;
    width: 1200px;
    height: 693px;
    overflow: hidden;
    background: var(--page);
  }
  .card {
    position: absolute;
    left: 46px;
    top: 48px;
    width: 1121px;
    height: 608px;
    background: linear-gradient(90deg, var(--card) 0%, var(--card) 60%, var(--card-light) 100%);
    overflow: hidden;
    color: var(--ink);
  }
  .bands {
    position: absolute;
    inset: 0;
    width: 1121px;
    height: 608px;
  }
  .identity {
    position: absolute;
    left: 62px;
    top: 74px;
    margin: 0;
  }
  .name {
    margin: 0;
    font-family: "Open Sans", sans-serif;
    font-weight: 700;
    font-size: 62px;
    line-height: 64px;
    letter-spacing: 13px;
    white-space: nowrap;
  }
  .name .surname { color: var(--accent); }
  .role {
    margin: 2px 0 0 2px;
    font-family: "Open Sans", sans-serif;
    font-weight: 700;
    font-size: 27px;
    letter-spacing: 6px;
    white-space: nowrap;
  }
  .contacts {
    position: absolute;
    left: 62px;
    top: 257px;
    margin: 0;
    padding: 0;
    list-style: none;
    font-family: "PT Sans Narrow", sans-serif;
    font-size: 42px;
    white-space: nowrap;
  }
  .contact {
    display: flex;
    align-items: center;
    height: 62.5px;
  }
  .contact-icon {
    width: 52px;
    height: 52px;
    margin-right: 14px;
    flex: none;
  }
  .social-mark {
    width: 44px;
    height: 44px;
    margin: 0 18px 0 4px;
    border: 2px solid var(--ink);
    border-radius: 5px;
    box-sizing: border-box;
    flex: none;
  }
</style>
</head>
<body>
  <main class="card">
    <svg class="bands" viewBox="0 0 1121 608" aria-hidden="true">
      <polygon points="1072,0 1080,0 606,608 594,608" fill="var(--band-orange-edge)"/>
      <polygon points="1023,0 1072,0 594,608 392,608" fill="var(--band-orange)"/>
      <polygon points="1121,40 1121,60 785,608 769,608" fill="var(--band-grey-edge)"/>
      <polygon points="1086,0 1121,0 1121,40 769,608 617,608" fill="var(--band-grey)"/>
    </svg>

    <header class="identity">
      <h1 class="name">MIRANDA <span class="surname">VOSS</span></h1>
      <p class="role">PRINCIPAL COACH &amp; CONSULTANT</p>
    </header>

    <ul class="contacts">
      <li class="contact">
        <svg class="contact-icon" viewBox="0 0 52 52" aria-label="Phone">
          <rect x="8" y="6" width="38" height="42" rx="4" fill="var(--ink)"/>
          <rect x="4" y="12" width="8" height="3" fill="var(--ink)"/>
          <rect x="4" y="24" width="8" height="3" fill="var(--ink)"/>
          <rect x="4" y="36" width="8" height="3" fill="var(--ink)"/>
          <circle cx="28" cy="22" r="6" fill="var(--card)"/>
          <path d="M17 39 q11 -16 22 0 z" fill="var(--card)"/>
        </svg>
        <span>0491 362 815</span>
      </li>
      <li class="contact">
        <svg class="contact-icon" viewBox="0 0 52 52" aria-label="Email">
          <rect x="2" y="12" width="48" height="30" fill="var(--ink)"/>
          <path d="M5 15 L26 31 L47 15" fill="none" stroke="var(--card)" stroke-width="2.5"/>
          <path d="M5 39 L20 26 M47 39 L32 26" fill="none" stroke="var(--card)" stroke-width="2.5"/>
        </svg>
        <span>miranda.voss@quillmail.example</span>
      </li>
      <li class="contact">
        <span class="social-mark" aria-hidden="true"></span>
        <span>updates.example/</span>
      </li>
      <li class="contact">
        <span class="social-mark" aria-hidden="true"></span>
        <span>friends.example/</span>
      </li>
      <li class="contact">
        <span class="social-mark" aria-hidden="true"></span>
        <span>network.example/</span>
      </li>
    </ul>
  </main>
</body>
</html>
```